Quick Straightforward Billboard Redesign

- Design billboard sized for 10 foot' x 36' foot width live area size and please include bleeds 6" around all sides
- Exact blue color match is imperative in headline, logo, phone number bubble or wherever used. C-83 / M-45 / Y-1 / K-0-
- What I hope to illustrate is that our company offers the best porch screening in the area area, in regards to quality, expertise, durability, storms proof, but we do not build screen porches.
- Current board is attached below from previous designer, and as you can see sizing was off, white space on edges make it appear to be sized incorrectly.
- I also attached my own little mock up idea well well if it helps, favorite image, logo, headline, etc and ideas perhaps on expanding or making this better?

Thanks so much!

Target Market(s)

Drivers and passengers, Southeastern NC, are of immense new construction and high end homes.

Industry/Entity Type

Construction

Colors
0054AA
0677BA
7BADD7
CADEEF
E8F1F8

Requirements
Must have
• Blue color matching
Nice to have
• Design spins or other thoughts on my little mock up

```html
<!DOCTYPE html>
<html lang="en">
<head>
<meta charset="utf-8">
<title>Harbor Porch Co. Billboard</title>
<link rel="stylesheet" href="https://fonts.googleapis.com/css2?family=Jost:wght@700&family=Oswald:wght@700&family=Lexend:wght@500&display=swap">
<style>
  :root {
    --brand-blue: #0068ac;
    --brand-green: #00b760;
    --ink: #262626;
    --backdrop: #f1edf1;
    --paper: #ffffff;
    --frame: #555555;
  }
  * { margin: 0; padding: 0; box-sizing: border-box; }
  html, body { width: 1200px; height: 1200px; overflow: hidden; background: var(--backdrop); }
  .mount {
    position: absolute; left: 0; top: 421px; width: 1200px; height: 357px;
    background: var(--paper);
  }
  .billboard {
    position: absolute; left: 16px; top: 17px; width: 1168px; height: 324px;
    border: 1px solid var(--frame); background: var(--paper); overflow: hidden;
  }
  .headline {
    position: absolute; left: 19px; top: 8px;
    font-family: "Jost", "Futura", sans-serif; font-weight: 700;
    font-size: 82px; line-height: 72px; letter-spacing: 0.5px; white-space: nowrap;
  }
  .headline .line-one { color: var(--brand-blue); display: block; }
  .headline .line-two { color: var(--brand-green); display: block; }
  .brand-name {
    position: absolute; left: 20px; top: 208px;
    font-family: "Jost", "Futura", sans-serif; font-weight: 700; color: var(--brand-blue);
    font-size: 46px; line-height: 60px; white-space: nowrap;
  }
  .features {
    position: absolute; left: 448px; top: 170px; list-style: none;
    font-family: "Lexend", sans-serif; font-weight: 500; color: var(--ink);
    font-size: 14px; line-height: 16.5px; letter-spacing: -0.3px; text-transform: uppercase;
  }
  .features li { position: relative; padding-left: 22px; margin-bottom: 4px; }
  .features svg { position: absolute; left: 0; top: 1px; width: 16px; height: 16px; }
  .porch-photo {
    position: absolute; left: 757px; top: 0; width: 411px; height: 324px;
    background: linear-gradient(180deg, #eef0f1 0%, #dfe3e6 28%, #8fc0ec 40%, #5a8a4c 50%, #9fbf86 62%, #8a8378 72%, #c7bfb2 100%);
  }
  .phone-badge {
    position: absolute; left: 896px; top: 250px; width: 253px; height: 60px;
    background: var(--brand-blue); border-radius: 10px;
    display: flex; align-items: center; justify-content: center;
    font-family: "Oswald", sans-serif; font-weight: 700; color: #ffffff;
    font-size: 42px; letter-spacing: -0.5px;
  }
</style>
</head>
<body>
  <div class="mount">
    <div class="billboard">
      <h1 class="headline">
        <span class="line-one">Screen Your Porch</span>
        <span class="line-two">Built for the Coast.</span>
      </h1>

      <div class="brand-name">Harbor Porch Co.</div>

      <ul class="features">
        <li><svg viewBox="0 0 16 16"><circle cx="8" cy="8" r="6.5" fill="none" stroke="#0068ac" stroke-width="1.6"/><path d="M4.8 8.2l2.3 2.3 5.6-6" fill="none" stroke="#0068ac" stroke-width="1.8"/></svg>High-durability<br>screen systems</li>
        <li><svg viewBox="0 0 16 16"><circle cx="8" cy="8" r="6.5" fill="none" stroke="#0068ac" stroke-width="1.6"/><path d="M4.8 8.2l2.3 2.3 5.6-6" fill="none" stroke="#0068ac" stroke-width="1.8"/></svg>Advanced storm<br>protection</li>
        <li><svg viewBox="0 0 16 16"><circle cx="8" cy="8" r="6.5" fill="none" stroke="#0068ac" stroke-width="1.6"/><path d="M4.8 8.2l2.3 2.3 5.6-6" fill="none" stroke="#0068ac" stroke-width="1.8"/></svg>Invisible &amp; superior<br>clarity</li>
        <li><svg viewBox="0 0 16 16"><circle cx="8" cy="8" r="6.5" fill="none" stroke="#0068ac" stroke-width="1.6"/><path d="M4.8 8.2l2.3 2.3 5.6-6" fill="none" stroke="#0068ac" stroke-width="1.8"/></svg>Professional<br>installation expertise</li>
      </ul>

      <div class="porch-photo" role="img" aria-label="Photo of a covered porch with white ceiling, ceiling fan, wicker lounge furniture and a palm, overlooking a lawn and lake"></div>

      <div class="phone-badge">910.555.0142</div>
    </div>
  </div>
</body>
</html>
```